Name card for fertilizer industry

We 1. produce liquid fertilizer 2. gardening supply 3. Import&Export gardening related product.
I want the name card double-sided(Chinese & English version)
detail has chinese charactor for name and address.
Updates
Target Market(s)
Farmers
Industry/Entity Type
Industry
Contact Information for Business Card
Name: Martin Lo (邱偉達)
TEL: +886-47-615204
FAX:+886-47-640173
MOBILE: +886-952-184-603
ADDRESS: No.58, Taoyuan Rd, Beiming Township, Lanping County , TAIWAN(R.O.C) 蘭平縣北明鎮桃源路58號
Look and feel
Each slider illustrates characteristics of the customer's brand and the style your logo design should communicate.

```html
<!DOCTYPE html>
<html lang="en">
<head>
<meta charset="utf-8">
<title>Ling Hua Chemical Company – Name Cards</title>
<link rel="stylesheet" href="https://fonts.googleapis.com/css2?family=Cinzel:wght@600&family=Open+Sans:wght@400;700&family=Noto+Sans+TC:wght@400;500&display=swap">
<style>
  :root {
    --backdrop: #000000;
    --card: #ffffff;
    --green: #8dc63f;
    --green-light: #a6ce39;
    --green-deep: #74a533;
    --ink: #222222;
    --grey: #555555;
    --white: #ffffff;
  }
  * { margin: 0; padding: 0; box-sizing: border-box; }
  html, body {
    width: 1200px; height: 1000px; overflow: hidden;
    background: var(--backdrop);
    font-family: "Open Sans", Arial, sans-serif;
  }
  .stage { position: relative; width: 1200px; height: 1000px; }
  .card { position: absolute; background: var(--card); overflow: hidden; }
  .card--front { left: 78px; top: 67px; width: 690px; height: 448px; }
  .card--back { left: 481px; top: 582px; width: 622px; height: 405px; }
  .card__art { position: absolute; inset: 0; }

  .brand { position: absolute; text-align: center; line-height: 1.1; }
  .brand__mark { border-radius: 50%; background: var(--green); margin: 0 auto; }
  .brand__name { font-size: 40px; font-weight: 700; color: var(--green); letter-spacing: 0.5px; }
  .brand__sub { font-size: 20px; font-weight: 400; color: var(--grey); }
  .card--front .brand { left: 297px; top: 62px; width: 280px; }
  .card--front .brand__mark { width: 110px; height: 110px; margin-bottom: 34px; }
  .card--back .brand { left: 345px; top: 28px; width: 278px; }
  .card--back .brand__mark { width: 120px; height: 120px; margin-bottom: 30px; }

  .contact { position: absolute; left: 64px; font-size: 18px; color: var(--ink); white-space: nowrap; }
  .contact--mobile { top: 213px; }
  .contact--tel { top: 286px; }
  .contact--fax { top: 350px; }
  .contact--mail { top: 409px; }
  .address {
    position: absolute; left: 64px; top: 244px; width: 240px;
    font-size: 12px; line-height: 16px; color: var(--grey);
  }

  .holder {
    position: absolute; font-family: "Cinzel", Georgia, serif; font-weight: 600;
    font-size: 34px; letter-spacing: 1px; text-align: center; line-height: 1.2;
  }
  .holder__dots { display: flex; gap: 5px; justify-content: center; margin-top: 2px; }
  .holder__dots span { width: 10px; height: 10px; border-radius: 50%; background: currentColor; }
  .card--front .holder { left: 297px; top: 350px; width: 320px; color: var(--white); }
  .card--front .holder__dots span { background: var(--green-deep); }
  .card--back .holder { left: 72px; top: 322px; width: 230px; color: var(--green-deep); }

  .holder-cn {
    position: absolute; left: 72px; top: 280px; width: 230px; text-align: center;
    font-family: "Noto Sans TC", sans-serif; font-weight: 500; font-size: 24px;
    letter-spacing: 4px; color: var(--green-deep);
  }
  .address-cn {
    position: absolute; right: 24px; top: 360px;
    font-family: "Noto Sans TC", sans-serif; font-size: 16px; color: var(--grey);
  }
</style>
</head>
<body>
<main class="stage">

  <section class="card card--front" aria-label="English side">
    <svg class="card__art" width="690" height="448" viewBox="0 0 690 448" aria-hidden="true">
      <defs>
        <linearGradient id="bandFill" x1="0" x2="1">
          <stop offset="0" stop-color="#8dc63f"/>
          <stop offset="1" stop-color="#a6ce39"/>
        </linearGradient>
      </defs>
      <rect x="20" y="0" width="5" height="225" fill="#8dc63f"/>
      <rect x="33" y="0" width="5" height="420" fill="#8dc63f"/>
      <path d="M297 341 H595 Q670 360 690 448 H297 Z" fill="url(#bandFill)"/>
      <g fill="#8dc63f">
        <circle cx="30" cy="225" r="16"/>
        <circle cx="30" cy="297" r="16"/>
        <circle cx="30" cy="361" r="16"/>
        <circle cx="31" cy="421" r="16"/>
      </g>
      <g fill="none" stroke="#fff" stroke-width="1.6">
        <rect x="25" y="214" width="10" height="20" rx="1.5"/>
        <line x1="27" y1="219" x2="33" y2="219"/>
        <path d="M24 290 q-2 8 6 16 l3 -3 -3 -4 -2 1 q-3 -4 -3 -7 l2 -1 -1 -4 z" fill="#fff"/>
        <rect x="21" y="358" width="18" height="9" rx="1"/>
        <rect x="25" y="353" width="10" height="6"/>
        <rect x="22" y="415" width="18" height="12" rx="1.5"/>
        <polyline points="22,416 31,423 40,416"/>
      </g>
    </svg>

    <div class="brand">
      <div class="brand__mark"></div>
      <div class="brand__name">LING HUA</div>
      <div class="brand__sub">CHEMICAL COMPANY</div>
    </div>

    <p class="contact contact--mobile">+886-952-184-603</p>
    <p class="address">No.58, Taoyuan Rd, Beiming Township, Lanping County, TAIWAN (R.O.C)</p>
    <p class="contact contact--tel">+886-47-615204</p>
    <p class="contact contact--fax">+886-47-640173</p>
    <p class="contact contact--mail">martin0528@mailbox.com</p>

    <div class="holder">
      <p class="holder__name">Martin Lo</p>
      <div class="holder__dots"><span></span><span></span><span></span><span></span></div>
    </div>
  </section>

  <section class="card card--back" aria-label="Chinese side">
    <svg class="card__art" width="622" height="405" viewBox="0 0 622 405" aria-hidden="true">
      <rect x="19" y="0" width="5" height="340" fill="#8dc63f"/>
      <rect x="30" y="0" width="5" height="268" fill="#8dc63f"/>
      <circle cx="38" cy="278" r="14" fill="#74a533"/>
      <circle cx="21" cy="342" r="15" fill="#74a533"/>
    </svg>

    <div class="brand">
      <div class="brand__mark"></div>
      <div class="brand__name">LING HUA</div>
      <div class="brand__sub">CHEMICAL COMPANY</div>
    </div>

    <p class="holder-cn" lang="zh-Hant">邱偉達</p>
    <div class="holder">
      <p class="holder__name">Martin Lo</p>
      <div class="holder__dots"><span></span><span></span><span></span><span></span></div>
    </div>

    <p class="address-cn" lang="zh-Hant">蘭平縣北明鎮桃源路58號</p>
  </section>

</main>
</body>
</html>
```